Logo, Website, Headed Paper, Business Cards and e-Mail signature

Launching a business called "TRIL", a foreign exchange “Clearing House”.

We need urgently:
- business logo
- Wordpress 4.5.2 responsive homepage + template
- headed paper templates for LibreOffice + Google Docs
- business cards
- e-Mail signature

Note: only design, will do the html integration ourselves.

Brief & guidelines:
Our target audience are financial institutions (medium to very large), some very savvy, some more conservative. Corporate image needs to be clean and trustworthy, yet the business is a disruptor concept based on "blockchain" technology that comes from the Quorlex world.
The difficulty is to mix the Fintech attraction of cryptocurrencies and blockchain with the seriousness of investment banking finance.

=> Big no-no: cannot look like a retail foreign exchange business offering! TRIL is strictly an institutional service, no cute banknote design or graphics suggesting travel service etc.

TRIL image should =
50% Technology "Fintech"
20% Financial markets utility
15% Foreign Exchange
10% Settlement security
5% Investment Banking service

Explanations:
* Technology "Fintech" -> TRIL is a startup, and fits the "Fintech" profile. The Clearing House uses new technology (Blockchain) to settle FX transactions between participants.
* Financial markets utility -> A "Clearing house" is a central counterparty that helps effect all payments between participants by being the central hub for all transactions.
* Foreign Exchange -> Our service is exclusively focused on Spot Foreign Exchange
* Settlement security -> The role of the clearing house is to guarantee that everyone gets paid. It collects security deposits from participants to protect all sides from anyone's default. A good clearing house is rock solid and trusted by everyone.
* Investment Banking service -> TRIL only offers its service to institutions. Accredited investors only !

business logo
Letter based logo (TRIL obviously) and optionally full words "Torvane Ridge Interlink" as well. Don't worry about being BORING, this is not Zuppa-Mora and we don't need to appeal to the general public. Need to be easily recognised though...

Wordpress 4.5.2 compatible responsive homepage + template
Our web engineer uses that Wordpress version. The homepage is a "long scroll" with most info in sections as most startups in Silicon valley. Additional pages (template) added and accessible via the navigation menu.

Headed paper LibreOffice + Google Docs
Consistent branding templates for text editors LibreOffice and Google Docs.

Business cards
Either single or 2 sided, bit more freedom for the design. We need space for ->
Phone: mobile: e-Mail: Skype: Address: SIP: Slack: Google:
Could include a QR code on the back side for the tech savvy (example file attached).

e-Mail signature
HTML signature that we will use with Thunderbird, containing details of the business card plus possibly a short legal disclaimer.

Example web sites and why we like them:
https://www.brimvalehost.com/features/networking/
Clean, white spaces, not too much text (no one reads much these days), graphics do the explaining.
https://www.pallisk.com/
The best (apart from the childish graphics). Long scroll, graphics that explain, colour delimited sections, links to more resources, simple top navigation.
https://veridoor.org/how-it-works/
Clean and simple header, tech graphics. Don't like full width text and no sections.
http://www.kmr.com/home
Only Financial site we don't dislike too much. It is clean and simple, not too cramped and feels friendly. Not very high-tech though...

Some Blockchain related sites and mix graphics, no particular likes, but just to give ideas on how others have captured the tech image of Blockchain/Distributed-ledger:
http://zp.vu/7Hq3mTa
http://zp.vu/4Rk8nYe
http://zp.vu/9Jw2pLd
http://zp.vu/3Vn5xQb
=> Careful not to fall into "The Lantern" trap. Technology mastery, not MYSTERY. The presence of numbers could allow to put recognisable FX prices if need be. We don’t like dark/black backgrounds in general...

Target Market(s)

Our target audience are financial institutions (medium to very large), some very savvy, some more conservative.

Industry/Entity Type

Financial Service

Contact Information for Business Card

Either single or 2 sided, bit more freedom for the design than the Website. We need space for ->

Logo Text

TRIL (optionally can add "The Torvane Ridge Interlink")

Number of Pages Required

2 page

Font styles to use
Sans Serif

Requirements
Must have
• Wordpress 4.5.2 compatible responsive homepage
• Our web engineer uses that Wordpress version. The homepage is a "long scroll" with most info in sections as most startups in Silicon valley.
• Additional pages: accessible via the navigation menu, based on 1 template that we would like you to design.
Should not have
• Cannot look like a retail (private investor) foreign exchange business offering! TRIL is strictly an institutional service, no cute banknote designs or graphics suggesting travel service etc.

```html
<!DOCTYPE html>
<html lang="en">
<head>
<meta charset="utf-8">
<title>TRIL — Torvane Ridge Interlink</title>
<link href="https://fonts.googleapis.com/css2?family=Raleway:wght@500;600;700&family=Open+Sans:wght@400;600;700&display=swap" rel="stylesheet">
<style>
:root{
  --orange:#e46b45;
  --orange-text:#e2701f;
  --green:#6cb049;
  --green-text:#6aa84a;
  --ink:#2b2b2b;
  --body:#444;
  --grey-band:#efefef;
  --white:#fff;
  --footer:#25282b;
  --footer-text:#9a9ea2;
  --footer-line:#393c40;
  --peach:#fbd9c9;
}
*{margin:0;padding:0;box-sizing:border-box}
html,body{width:1200px;height:2239px;overflow:hidden}
body{position:relative;background:var(--white);font-family:"Open Sans",Arial,sans-serif;color:var(--body)}
.abs{position:absolute}

/* Header */
.topline{left:0;top:0;width:1200px;height:3px;background:var(--orange)}
.site-header{left:0;top:3px;width:1200px;height:79px;background:var(--white)}
.brand{left:160px;top:28px;font-family:"Raleway",sans-serif;font-weight:700;font-size:25px;color:var(--ink);letter-spacing:.5px}
.nav a{position:absolute;top:38px;font-family:"Raleway",sans-serif;font-weight:600;font-size:12px;color:var(--ink);text-decoration:none;letter-spacing:.3px}
.nav a.current{color:var(--orange)}
.signup{left:960px;top:25px;width:76px;height:35px;background:var(--green);color:var(--white);font-family:"Raleway",sans-serif;font-weight:600;font-size:12px;display:flex;align-items:center;justify-content:center}

/* Hero */
.hero{left:0;top:82px;width:1200px;height:579px;overflow:hidden}
.hero-photo{position:absolute;inset:0;background:
  radial-gradient(ellipse at 70% 20%,#4a3a3e 0%,transparent 45%),
  radial-gradient(ellipse at 35% 55%,#7b8280 0%,transparent 40%),
  linear-gradient(160deg,#5d6b35 0%,#44502a 40%,#3a3f2c 70%,#2d2f28 100%)}
.hero-shade{position:absolute;inset:0;background:rgba(20,22,18,.28)}
.hero-title{left:0;top:205px;width:1200px;text-align:center;font-family:"Raleway",sans-serif;font-weight:700;font-size:51px;color:var(--white)}
.hero-lead{left:0;top:272px;width:1200px;text-align:center;font-family:"Raleway",sans-serif;font-weight:500;font-size:21px;line-height:27px;color:var(--white)}
.hero-cta{left:484px;top:349px;width:232px;height:51px;background:var(--orange);color:var(--white);font-family:"Raleway",sans-serif;font-weight:700;font-size:17px;display:flex;align-items:center;justify-content:center}
.dot{top:529px;width:20px;height:20px;border-radius:50%;background:rgba(255,255,255,.55)}
.dot.active{background:var(--white)}

/* Feature grid */
.features{left:0;top:661px;width:1200px;height:876px}
.feature-shapes{position:absolute;left:0;top:0}
.art{position:absolute;border-radius:50%}
.art-light{background:radial-gradient(circle at 50% 50%,#e3e6e8 0%,#e9ebec 55%,rgba(239,239,239,0) 72%)}
.art-white{background:radial-gradient(circle at 50% 50%,#eef0ef 0%,#f3f4f3 55%,rgba(255,255,255,0) 72%)}
.art-orange{background:radial-gradient(circle at 50% 50%,#ec8a68 0%,#e97d59 55%,rgba(228,107,69,0) 72%)}
.feature-title{position:absolute;width:520px;text-align:center;font-family:"Raleway",sans-serif;font-weight:600;font-size:25px}
.feature-text{position:absolute;width:520px;text-align:center;font-size:12.5px;line-height:21px;color:var(--body)}
.t-orange{color:var(--orange-text)}
.t-green{color:var(--green-text)}
.t-white{color:var(--white)}
.txt-peach{color:var(--peach)}

/* Settlement */
.settle-title{left:161px;top:1668px;font-family:"Raleway",sans-serif;font-weight:600;font-size:25px;color:var(--orange-text)}
.settle-text{left:161px;top:1718px;width:460px;font-size:12.5px;line-height:21.5px;color:var(--body)}

/* Footer */
.site-footer{left:0;top:1915px;width:1200px;height:324px;background:var(--footer)}
.f-head{position:absolute;top:47px;font-weight:700;font-size:11.5px;color:var(--white)}
.f-about{left:161px;top:82px;width:270px;font-size:10.5px;line-height:19px;color:var(--footer-text)}
.f-list{position:absolute;top:82px;list-style:none}
.f-list li{font-size:10.5px;line-height:18.7px;color:var(--footer-text)}
.signup-form{left:161px;top:157px;width:252px;height:34px;border:1px solid #c9ccce;background:var(--footer);display:flex}
.signup-form span{flex:1;padding-left:8px;font-size:10.5px;color:var(--white);line-height:32px}
.signup-form b{width:41px;background:var(--green);color:var(--white);font-size:11px;display:flex;align-items:center;justify-content:center}
.f-rule{left:161px;top:251px;width:879px;height:1px;background:var(--footer-line)}
.social{top:283px;width:20px;height:20px;border-radius:50%;border:1.5px solid #7d8287}
.copyright{right:160px;top:284px;font-size:10.5px;color:var(--footer-text)}
</style>
</head>
<body>

<div class="abs topline"></div>
<header class="abs site-header">
  <div class="abs brand">TRIL</div>
  <nav class="nav">
    <a class="current" style="left:407px">HOME</a>
    <a style="left:490px">FPRICING</a>
    <a style="left:591px">FEATURES</a>
    <a style="left:695px">COMMUNITY</a>
    <a style="left:816px">HELP</a>
    <a style="left:891px">LOGIN</a>
  </nav>
  <div class="abs signup">SIGN UP</div>
</header>

<section class="abs hero">
  <div class="hero-photo" role="img" aria-label="Photo of a person sitting on the grass typing on a laptop beside a coffee cup"></div>
  <div class="hero-shade"></div>
  <h1 class="abs hero-title">TORVANE RIDGE INTERLINK</h1>
  <p class="abs hero-lead">Lorem ipsum dolor sit amet, consectetur adipiscing elit, sed do<br>eiusmod tempor incididunt ut labore et dolore magna aliqua.</p>
  <div class="abs hero-cta">GET STARTED HERE</div>
  <span class="abs dot active" style="left:550px"></span>
  <span class="abs dot" style="left:577px"></span>
  <span class="abs dot" style="left:603px"></span>
  <span class="abs dot" style="left:629px"></span>
</section>

<section class="abs features">
  <svg class="feature-shapes" width="1200" height="876" viewBox="0 0 1200 876">
    <polygon points="0,0 552,0 654,439 0,439" fill="var(--grey-band)"/>
    <polygon points="0,439 654,439 567,876 0,876" fill="#f2f2f2"/>
    <polygon points="654,439 1200,439 1200,876 567,876" fill="var(--orange)"/>
    <line x1="0" y1="439" x2="1200" y2="439" stroke="#e2e2e2"/>
  </svg>

  <div class="art art-light" role="img" aria-label="Illustration of computer screens with code windows" style="left:250px;top:44px;width:180px;height:180px"></div>
  <h2 class="feature-title t-orange" style="left:86px;top:242px">Technology "Fintech"</h2>
  <p class="feature-text" style="left:86px;top:293px">TRIL is a startup, and fits the "Fintech" profile. The<br>Clearing House uses new technology (Blockchain) to settle<br>FX transactions between participants.</p>

  <div class="art art-white" role="img" aria-label="Illustration of a briefcase with calculator, documents and finance icons" style="left:767px;top:44px;width:180px;height:180px"></div>
  <h2 class="feature-title t-green" style="left:597px;top:242px">Financial markets utility</h2>
  <p class="feature-text" style="left:597px;top:293px">A "Clearing house" is a central counterparty that<br>helps effect all payments between participants by being<br>the central hub for all transactions.</p>

  <div class="art art-light" role="img" aria-label="Illustration of a calculator, charts report and glasses on a desk" style="left:250px;top:490px;width:190px;height:190px"></div>
  <h2 class="feature-title t-green" style="left:86px;top:700px">Foreign Exchange</h2>
  <p class="feature-text" style="left:86px;top:752px">Our service is exclusively focused on Spot Foreign Exchange</p>

  <div class="art art-orange" role="img" aria-label="Illustration of a mobile phone, receipts, coins and a clock" style="left:762px;top:486px;width:190px;height:190px"></div>
  <h2 class="feature-title t-white" style="left:597px;top:700px">Investment Banking service</h2>
  <p class="feature-text txt-peach" style="left:597px;top:754px">TRIL only offers its service to institutions.<br>Accredited investors only !</p>
</section>

<h2 class="abs settle-title">Settlement security</h2>
<p class="abs settle-text">&nbsp;The role of the clearing house is to guarantee that everyone gets paid. It collects security deposits from participants to protect all sides from anyone's default. A good clearing house is rock solid and trusted by everyone.</p>
<div class="abs art art-white" role="img" aria-label="Illustration of hands holding a tablet showing a privacy lock screen" style="left:724px;top:1614px;width:250px;height:250px"></div>

<footer class="abs site-footer">
  <h3 class="f-head" style="left:161px">TORVANE RIDGE INTERLINK</h3>
  <p class="abs f-about">Lorem ipsum dolor sit amet, consectetur adipiscing elit, sed do eiusmod tempor incididunt ut laborerem ipsum dolor sit amet, consectetur adipiscin.</p>
  <div class="abs signup-form"><span>Email:</span><b>GO</b></div>

  <h3 class="f-head" style="left:501px">PRODUCT</h3>
  <ul class="f-list" style="left:501px"><li>Pricing</li><li>Features</li><li>Customers</li><li>One-Click Apps</li><li>API</li></ul>

  <h3 class="f-head" style="left:645px">COMPANY</h3>
  <ul class="f-list" style="left:645px"><li>About Us</li><li>Blog</li><li>Careers</li><li>Press</li><li>Events</li><li>Logos &amp; Badges</li><li>Contact</li></ul>

  <h3 class="f-head" style="left:795px">HELP</h3>
  <ul class="f-list" style="left:795px"><li>Getting Started</li><li>Feedback</li><li>Referral Program</li><li>Network Status</li><li>FAQ</li></ul>

  <h3 class="f-head" style="left:952px">COMMUNITY</h3>
  <ul class="f-list" style="left:952px"><li>Dashboard</li><li>Tutorials</li><li>Questions</li><li>Projects</li><li>Get Paid to Write</li></ul>

  <div class="abs f-rule"></div>
  <span class="abs social" style="left:165px"></span>
  <span class="abs social" style="left:199px"></span>
  <span class="abs social" style="left:232px"></span>
  <span class="abs social" style="left:266px"></span>
  <p class="abs copyright">© 2016 Torvane Ridge Interlink &nbsp;All right reserved &nbsp;Term of Use</p>
</footer>

</body>
</html>
```